Business Card Design

I have a very clear idea of what I want. I just do not know how to do the graphic design to match it.

On the front I want the uploaded image with the horse and the two people.
I want

Bottom left hand corner
Lewis Brand
0438 512 607

Bottom right
There is maroon block with Neil Patton Practitioner Group Logo
Next to that I want the Stable Arc tile about the same size ( attached psd file)

On the back I want a plain colour (white) with the information

Lewis Brand
Equine Performance
Rowland4Ponies and Acupuncture
Horsemanship Lessons and Clinics
Horse Training

lbrand@fauna812.com.au
FB/lewis.brand.207
StableArc.com.au

Industry/Entity Type

Business

Contact Information for Business Card

Lewis Brand
0438 512 607
lbrand@fauna812.com.au

```html
<!DOCTYPE html>
<html lang="en">
<head>
<meta charset="utf-8">
<title>Lewis Brand – Business Card</title>
<link rel="stylesheet" href="https://fonts.googleapis.com/css2?family=Noto+Sans:wght@400;600&family=Playfair+Display:wght@700&display=swap">
<style>
  :root {
    --page-bg: #dcdcdc;
    --card-white: #ffffff;
    --ink: #111111;
    --navy: #1d3461;
    --brown: #3a1c0c;
    --sand-light: #e3cfa9;
    --sand-dark: #b8946a;
    --gold-rule: #d9a96b;
    --cream: #f6eee2;
  }
  html, body {
    margin: 0;
    width: 1189px;
    height: 1200px;
    overflow: hidden;
    background: var(--page-bg);
  }
  .sheet {
    position: relative;
    width: 1189px;
    height: 1200px;
  }
  .card {
    position: absolute;
    left: 140px;
    width: 918px;
    height: 524px;
    box-shadow: 0 6px 14px rgba(0,0,0,0.35);
    background: var(--card-white);
    overflow: hidden;
  }
  .card svg { display: block; width: 100%; height: 100%; }
  .card-contact { top: 45px; }
  .card-services { top: 624px; }
  .sans { font-family: "Noto Sans", Verdana, sans-serif; }
  .holder-name { font-size: 60px; font-weight: 600; fill: var(--ink); }
  .contact-line { font-size: 35px; fill: var(--ink); }
  .brand-name { font-size: 46px; font-weight: 600; fill: var(--navy); }
  .services-title { font-family: "Playfair Display", Georgia, serif; font-size: 54px; font-weight: 700; fill: var(--cream); }
  .service-item { font-size: 30px; fill: var(--cream); }
</style>
</head>
<body>
<div class="sheet">

  <section class="card card-contact" aria-label="Card side with contact details">
    <svg viewBox="0 0 1124 642" preserveAspectRatio="none">
      <text class="sans holder-name" x="52" y="103">Lewis Brand</text>

      <g class="contact-list">
        <rect x="56" y="352" width="22" height="22" fill="var(--navy)"/>
        <path d="M61 357 q2 9 12 12 l2-3 -4-2 -2 2 q-4-2-5-5 l2-2 -2-4z" fill="#fff"/>
        <text class="sans contact-line" x="95" y="377">0438 512 607</text>

        <rect x="56" y="403" width="22" height="22" fill="var(--navy)"/>
        <rect x="60" y="408" width="14" height="11" fill="#fff"/>
        <path d="M60 408 l7 6 7-6" fill="none" stroke="var(--navy)" stroke-width="1.5"/>
        <text class="sans contact-line" x="95" y="428">lbrand@fauna812.com.au</text>

        <rect x="56" y="454" width="22" height="22" fill="var(--navy)"/>
        <text class="sans contact-line" x="95" y="479">lewis.brand.207</text>

        <rect x="56" y="506" width="22" height="22" fill="var(--navy)"/>
        <circle cx="67" cy="517" r="7" fill="none" stroke="#fff" stroke-width="2"/>
        <text class="sans contact-line" x="95" y="531">StableArc.com.au</text>
      </g>

      <g class="brand-mark">
        <rect x="712" y="208" width="30" height="30" fill="var(--navy)"/>
        <text class="sans brand-name" x="756" y="238">Stable Arc</text>
      </g>

      <path class="swoosh-navy" d="M450 642 C800 612 1000 520 1124 405 L1124 642 Z" fill="var(--navy)"/>
      <path class="swoosh-brown" d="M0 572 C300 548 800 520 1124 380 L1124 394 C820 548 350 615 0 632 Z" fill="var(--brown)"/>
    </svg>
  </section>

  <section class="card card-services" aria-label="Card side with photo and services">
    <svg viewBox="0 0 1124 640" preserveAspectRatio="none">
      <defs>
        <linearGradient id="sand" x1="0" y1="0" x2="1" y2="1">
          <stop offset="0" stop-color="var(--sand-dark)"/>
          <stop offset="0.45" stop-color="var(--sand-light)"/>
          <stop offset="1" stop-color="var(--sand-dark)"/>
        </linearGradient>
      </defs>

      <rect class="photo-area" x="0" y="0" width="1124" height="448" fill="url(#sand)" role="img" aria-label="Photo of a sand arena with a trainer watching a woman lead a horse, with a hand-lettered slogan in the upper left"/>

      <rect class="services-band" x="0" y="448" width="1124" height="192" fill="var(--brown)"/>
      <text class="services-title" x="573" y="500" text-anchor="middle">Services</text>
      <line x1="316" y1="511" x2="829" y2="511" stroke="var(--gold-rule)" stroke-width="3"/>

      <g class="service-marker" fill="none" stroke="var(--cream)" stroke-width="2">
        <circle cx="58" cy="543" r="9"/><path d="M46 543h24M58 531v24"/>
        <circle cx="58" cy="588" r="9"/><path d="M46 588h24M58 576v24"/>
        <circle cx="1068" cy="543" r="9"/><path d="M1056 543h24M1068 531v24"/>
        <circle cx="1068" cy="590" r="9"/><path d="M1056 590h24M1068 578v24"/>
      </g>
      <text class="sans service-item" x="90" y="553">Equine Performance</text>
      <text class="sans service-item" x="90" y="598">Rowland4Ponies and Acupuncture</text>
      <text class="sans service-item" x="1040" y="553" text-anchor="end">Horsemanship Lessons and Clinics</text>
      <text class="sans service-item" x="1040" y="598" text-anchor="end">Horse Training</text>
    </svg>
  </section>

</div>
</body>
</html>
```